Deal Email Template Design

I need a number of email templates designed for my deal website. The emails will be used to promote, market, and sell it's deals. Emails will be launched using an email marketing platform. I will work with chosen designer to detail the company description, branding, logos, etc.
Updates
Reason: I added details to project and would like to see some more bids. Please feel free to submit and ask any questions.
Thank you.
Target Market(s)
Casino Destination Travelers
Industry/Entity Type
It Company
Look and feel
Each slider illustrates characteristics of the customer's brand and the style your logo design should communicate.

```html
<!DOCTYPE html>
<html lang="en">
<head>
<meta charset="utf-8">
<title>Rivermoor Newsletter</title>
<link rel="stylesheet" href="https://fonts.googleapis.com/css2?family=Arimo:wght@400;700&family=Carlito:wght@400;700&display=swap">
<style>
  :root {
    --page-bg: #0e1213;
    --brand-yellow: #e3c20c;
    --card-bg: #ffffff;
    --divider: #eceff0;
    --heading: #111111;
    --body-text: #7b8589;
    --partner-grey: #7d8385;
    --accent-red: #d9363a;
    --frame: #c9cfd1;
    --footer-link: #8a9396;
    --mark-grey: #5f6b6f;
  }
  * { margin: 0; padding: 0; box-sizing: border-box; }
  html, body { width: 1000px; height: 1200px; overflow: hidden; }
  body { background: var(--page-bg); position: relative; font-family: "Arimo", Arial, sans-serif; }

  .site-header { position: absolute; left: 200px; top: 12px; width: 600px; height: 40px; }
  .brand { position: absolute; left: 0; top: 2px; display: flex; align-items: center; gap: 10px; }
  .brand-dot { width: 30px; height: 30px; border-radius: 50%; background: var(--brand-yellow); }
  .brand-text { position: relative; }
  .brand-name { display: block; font-family: "Carlito", sans-serif; font-weight: 700; font-size: 22px; line-height: 22px; color: var(--brand-yellow); }
  .brand-sub { position: absolute; right: 0; top: 20px; font-family: "Carlito", sans-serif; font-size: 13px; line-height: 13px; color: var(--brand-yellow); }
  .top-nav { position: absolute; right: 2px; top: 9px; font-family: "Carlito", sans-serif; font-size: 17px; color: var(--brand-yellow); }
  .top-nav a { color: inherit; text-decoration: none; }

  .email-card { position: absolute; left: 200px; top: 69px; width: 601px; height: 1032px; background: var(--card-bg); border-radius: 4px; overflow: hidden; }

  .hero { position: absolute; left: 0; top: 0; width: 100%; height: 254px;
    background: radial-gradient(ellipse at 70% 45%, #c4542a 0%, #8e2a16 45%, #4a140c 100%); }
  .hero-amount { position: absolute; left: 41px; top: 22px; font-size: 132px; line-height: 1; color: var(--brand-yellow); letter-spacing: -2px; }
  .hero-offer { position: absolute; left: 31px; top: 162px; font-size: 38px; line-height: 34px; color: var(--brand-yellow); }

  .section { position: absolute; left: 0; width: 100%; border-top: 1px solid var(--divider); }

  .partners { top: 254px; height: 77px; border-top: none; }
  .partner-name { position: absolute; top: 24px; width: 180px; text-align: center; font-size: 24px; color: var(--partner-grey); }

  .showcase { top: 331px; height: 150px; }
  .thumb { position: absolute; top: 27px; width: 150px; height: 97px; border: 1px solid var(--frame); padding: 3px; background: #fff; }
  .thumb-fill { width: 100%; height: 100%; }

  .features { top: 481px; height: 220px; }
  .feature { position: absolute; width: 150px; }
  .feature-title { display: flex; align-items: center; gap: 7px; font-size: 14px; font-weight: 700; color: var(--heading); height: 18px; }
  .feature-title svg { width: 14px; height: 14px; flex: none; }
  .feature-text { width: 140px; margin-top: 4px; font-size: 12px; line-height: 18px; color: var(--body-text); }

  .promo { top: 701px; height: 195px; }
  .promo-title { position: absolute; left: 47px; top: 28px; font-size: 14px; font-weight: 700; color: var(--heading); }
  .promo-text { position: absolute; left: 47px; top: 52px; width: 320px; font-size: 12px; line-height: 18px; color: var(--body-text); }
  .buy-button { position: absolute; left: 50px; top: 128px; width: 83px; height: 34px; border: 1px solid #dfe3e5; border-radius: 3px; background: linear-gradient(#ffffff, #f0f2f3); box-shadow: 0 1px 2px rgba(0,0,0,.08); font-size: 12px; font-weight: 700; color: #5a6366; text-align: center; line-height: 32px; }
  .promo-shot { position: absolute; left: 409px; top: 25px; width: 150px; height: 96px; border: 1px solid var(--frame); padding: 3px; background: #fff; }

  .site-footer { top: 896px; height: 136px; }
  .footer-col { position: absolute; top: 18px; font-family: "Carlito", sans-serif; font-size: 14px; }
  .footer-col h3 { font-size: 14px; font-weight: 400; line-height: 18px; color: var(--heading); margin-bottom: 3px; }
  .footer-col a { display: block; color: var(--footer-link); text-decoration: none; line-height: 24px; }
  .footer-mark { position: absolute; left: 447px; top: 33px; width: 64px; height: 64px; border-radius: 50%; background: var(--mark-grey); }
</style>
</head>
<body>
  <header class="site-header">
    <div class="brand"><span class="brand-dot"></span><span class="brand-text"><span class="brand-name">Rivermoor</span><span class="brand-sub">newsletter</span></span></div>
    <nav class="top-nav"><a href="#">Home</a> - <a href="#">About</a> - <a href="#">Contact</a></nav>
  </header>

  <main class="email-card">
    <section class="hero" role="img" aria-label="Blurred casino floor with gaming tables and slot machines in warm red light">
      <div class="hero-amount">$25</div>
      <div class="hero-offer">FREEPLAY for<br>New Members!</div>
    </section>

    <section class="section partners">
      <div class="partner-name" style="left:30px;">Calverne</div>
      <div class="partner-name" style="left:210px;">Tinkerly</div>
      <div class="partner-name" style="left:390px;">Dailyfold</div>
    </section>

    <section class="section showcase">
      <div class="thumb" style="left:47px;"><div class="thumb-fill" role="img" aria-label="Close-up of a metal microphone grille" style="background:linear-gradient(90deg,#8d9396,#d6dadc 45%,#3a3f42);"></div></div>
      <div class="thumb" style="left:228px;"><div class="thumb-fill" role="img" aria-label="App interface detail with red header and follower tabs" style="background:linear-gradient(#d8393b 0 42%,#3b4043 42%);"></div></div>
      <div class="thumb" style="left:409px;"><div class="thumb-fill" role="img" aria-label="Dark profile card interface detail" style="background:linear-gradient(90deg,#9a5a3c 0 35%,#1f2325 35%);"></div></div>
    </section>

    <section class="section features">
      <div class="feature" style="left:47px;top:25px;">
        <div class="feature-title"><svg viewBox="0 0 14 14"><rect x="3" y="0.5" width="8" height="13" rx="1.5" fill="var(--accent-red)"/><rect x="4.5" y="2.5" width="5" height="7" fill="#fff"/><circle cx="7" cy="11.5" r="0.9" fill="#fff"/></svg>Gestures</div>
        <p class="feature-text">Nullam id dolor id nibh ultricies vehicula ut id elit. Praesent commodo.</p>
      </div>
      <div class="feature" style="left:234px;top:25px;">
        <div class="feature-title"><svg viewBox="0 0 14 14"><path d="M7 0.5a5 5 0 0 1 5 5c0 3.5-5 8-5 8s-5-4.5-5-8a5 5 0 0 1 5-5z" fill="var(--accent-red)"/><circle cx="7" cy="5.5" r="1.8" fill="#fff"/></svg>Geo Location</div>
        <p class="feature-text">Etiam porta sem malesuada magna mollis euismod Maas sed diam.</p>
      </div>
      <div class="feature" style="left:421px;top:25px;">
        <div class="feature-title"><svg viewBox="0 0 14 14"><rect x="1" y="2" width="11" height="11" rx="1.5" fill="none" stroke="var(--accent-red)" stroke-width="2"/><path d="M4 7l2.5 2.5L13 2" fill="none" stroke="var(--accent-red)" stroke-width="2"/></svg>Checkmarks</div>
        <p class="feature-text">Nullam id dolor id nibh ultricies vehicula ut id elit. Praesent commodo.</p>
      </div>
      <div class="feature" style="left:47px;top:121px;">
        <div class="feature-title"><svg viewBox="0 0 14 14" fill="var(--accent-red)"><rect x="0" y="1" width="3" height="3"/><rect x="5" y="1.5" width="9" height="2"/><rect x="0" y="5.5" width="3" height="3"/><rect x="5" y="6" width="9" height="2"/><rect x="0" y="10" width="3" height="3"/><rect x="5" y="10.5" width="9" height="2"/></svg>Lists</div>
        <p class="feature-text">Nullam id dolor id nibh ultricies vehicula ut id elit. Praesent commodo.</p>
      </div>
      <div class="feature" style="left:234px;top:121px;">
        <div class="feature-title"><svg viewBox="0 0 14 14" fill="var(--accent-red)"><ellipse cx="6" cy="5.5" rx="5.5" ry="4.5"/><path d="M2 8l-1.5 3.5L5 9.5z"/><ellipse cx="10" cy="10" rx="4" ry="3.3"/></svg>Conversations</div>
        <p class="feature-text">Etiam porta sem malesuada magna mollis euismod Maas sed diam.</p>
      </div>
      <div class="feature" style="left:421px;top:121px;">
        <div class="feature-title"><svg viewBox="0 0 14 14"><path d="M0.5 7C2.5 3.5 4.5 2.5 7 2.5S11.5 3.5 13.5 7C11.5 10.5 9.5 11.5 7 11.5S2.5 10.5 0.5 7z" fill="var(--accent-red)"/><circle cx="7" cy="7" r="2.3" fill="#fff"/></svg>Views</div>
        <p class="feature-text">Nullam id dolor id nibh ultricies vehicula ut id elit. Praesent commodo.</p>
      </div>
    </section>

    <section class="section promo">
      <h2 class="promo-title">Excellent Coding. Tested with Sendvane.</h2>
      <p class="promo-text">Maecenas faucibus mollis interdum. Donec ullamcorper nulla non metus auctor fringilla. Cras mattis consectetur purus sit amet fermentum.</p>
      <div class="buy-button">Buy Now</div>
      <div class="promo-shot"><div class="thumb-fill" role="img" aria-label="Dark interface panel showing an error message alert" style="background:linear-gradient(#33393c 0 40%,#1f2325 40%);"></div></div>
    </section>

    <footer class="section site-footer">
      <div class="footer-col" style="left:57px;">
        <h3>Navigation</h3>
        <a href="#">Home</a><a href="#">About us</a><a href="#">Open an account</a>
      </div>
      <div class="footer-col" style="left:211px;">
        <h3>More information</h3>
        <a href="#">Contact us</a><a href="#">F.A.Q.</a><a href="#">Testimonials</a>
      </div>
      <div class="footer-mark"></div>
    </footer>
  </main>
</body>
</html>
```